Modern card design needed for building development company

We are looking for a sharp modern new look for our business cards.
We are a New Zealand based company called TKV Ventures NZ LTD that specialises in subdividing large sections, housing and commercial buildings.
We have attached a photo of the current logo and would like to see it improved somehow as it looks a bit dated.
We are open to any colours.

Target Market(s)

Investors, Property buyers

Industry/Entity Type

Investment

Contact Information for Business Card

TKV VENTURES NZ LTD
www.tkvventuresnz.co.nz

Howard Pennick
Phone +64 21 843 192
Email hdpennick@fernmail.co.nz

Font styles to use
Serif
Sans Serif

Colors
0792cd
33a6d7
85cae6
6b449b
886aae
f04a50
ec1f27
f37122
f68d4d

Requirements
Must have
• Please try and make the logo more modern or if you have a similar one we would like to see it.

```html
<!DOCTYPE html>
<html lang="en">
<head>
<meta charset="utf-8">
<title>TKV Ventures NZ LTD – Business Cards</title>
<link rel="stylesheet" href="https://fonts.googleapis.com/css2?family=Roboto+Condensed:wght@300;400;700&display=swap">
<style>
  :root {
    --backdrop: #e4e4e4;
    --card-blue: #0a80bc;
    --mark-blue: #33a6d7;
    --ink-white: #ffffff;
    --rule-white: rgba(255,255,255,0.75);
  }
  * { box-sizing: border-box; margin: 0; padding: 0; }
  html, body { width: 1200px; height: 799px; overflow: hidden; }
  body {
    background: var(--backdrop);
    font-family: "Roboto Condensed", "Arial Narrow", sans-serif;
    color: var(--ink-white);
    position: relative;
  }
  .card {
    position: absolute;
    width: 500px;
    height: 290px;
    background: var(--card-blue);
    top: 254px;
    overflow: hidden;
  }
  .card--front { left: 70px; }
  .card--back { left: 630px; }

  .holder { position: absolute; top: 40px; right: 44px; text-align: right; }
  .holder__name { font-weight: 700; font-size: 22px; line-height: 1.2; }
  .holder__title { font-weight: 300; font-size: 14px; margin-top: 2px; }

  .brand {
    position: absolute;
    display: flex;
    align-items: center;
    gap: 12px;
    white-space: nowrap;
  }
  .card--front .brand { left: 44px; bottom: 48px; }
  .card--back .brand { left: 150px; top: 170px; }
  .brand__square {
    width: 26px; height: 26px;
    background: var(--mark-blue);
    flex: none;
  }
  .brand__name {
    font-weight: 700;
    font-size: 28px;
    line-height: 1.1;
    letter-spacing: 0.5px;
    text-transform: uppercase;
  }
  .card--back .brand__name { font-size: 22px; }

  .contact {
    position: absolute;
    top: 30px;
    right: 40px;
    width: 210px;
    font-weight: 300;
    font-size: 14px;
    line-height: 1.3;
  }
  .contact__group { padding: 6px 0; }
  .contact__group + .contact__group { border-top: 1px solid var(--rule-white); }
  .contact__group:last-child { border-bottom: 1px solid var(--rule-white); padding-bottom: 8px; }

  .website {
    position: absolute;
    left: 40px;
    bottom: 34px;
    font-weight: 700;
    font-size: 22px;
    line-height: 1.2;
    letter-spacing: 0.3px;
    white-space: nowrap;
  }
</style>
</head>
<body>
  <section class="card card--front" aria-label="Card front">
    <div class="holder">
      <p class="holder__name">Howard Pennick</p>
      <p class="holder__title">CEO</p>
    </div>
    <div class="brand">
      <span class="brand__square" aria-hidden="true"></span>
      <span class="brand__name">TKV Ventures NZ LTD</span>
    </div>
  </section>

  <section class="card card--back" aria-label="Card back">
    <div class="contact">
      <div class="contact__group">
        <p>PO Box 48215, Devonport</p>
        <p>Auckland, New Zealand.</p>
      </div>
      <div class="contact__group">
        <p>T: +64 21 843 192</p>
        <p>E: hdpennick@fernmail.co.nz</p>
      </div>
    </div>
    <div class="brand">
      <span class="brand__square" aria-hidden="true"></span>
      <span class="brand__name">TKV Ventures NZ LTD</span>
    </div>
    <p class="website">www.tkvventuresnz.co.nz</p>
  </section>
</body>
</html>
```